Moravel Stenwick Inc needs a business card design

Looking for a unique, classy and sharp business card design.

Contact Information for Business Card

Moravel Stenwick Inc.
Marisa Ortega Bellido BScOT(c)
Occupational Therapist
(780) 555-0142
moravelstenwick@postlynx.net

```html
<!DOCTYPE html>
<html lang="en">
<head>
<meta charset="utf-8">
<title>Moravel Stenwick Inc. – Business Card</title>
<link href="https://fonts.googleapis.com/css2?family=Arimo:wght@400;700&display=swap" rel="stylesheet">
<style>
  :root {
    --backdrop: #d9d9d9;
    --card: #ffffff;
    --plum: #8a2386;
    --leaf: #7cbf3f;
    --sky: #4aa8dc;
    --ink: #222222;
    --rule: #111111;
  }
  * { margin: 0; padding: 0; box-sizing: border-box; }
  html, body {
    width: 1200px; height: 923px; overflow: hidden;
    background: var(--backdrop);
    font-family: "Arimo", Arial, sans-serif;
  }
  .card {
    position: absolute; left: 110px; top: 181px;
    width: 980px; height: 560px;
    background: var(--card);
    box-shadow: 0 14px 40px rgba(0,0,0,.18);
  }
  .brand {
    position: absolute; top: 130px; left: 0; width: 100%;
    display: flex; justify-content: center; align-items: center; gap: 18px;
  }
  .brand-dot {
    width: 34px; height: 34px; border-radius: 50%; background: var(--leaf);
  }
  .brand-name {
    font-size: 52px; font-weight: 700; color: var(--plum); letter-spacing: -0.5px;
  }
  .divider {
    position: absolute; left: 545px; top: 262px;
    width: 3px; height: 150px; background: var(--rule);
  }
  .person {
    position: absolute; right: 460px; top: 330px; text-align: right;
  }
  .person-name { font-size: 25px; color: var(--plum); }
  .person-role { font-size: 21px; color: var(--sky); margin-top: 6px; }
  .contact {
    position: absolute; left: 575px; top: 268px; list-style: none;
  }
  .contact li {
    display: flex; align-items: center; gap: 14px;
    font-size: 21px; color: var(--ink); margin-bottom: 16px;
  }
  .contact-icon { width: 22px; height: 22px; flex: none; }
  .band {
    position: absolute; left: 0; top: 430px;
    width: 100%; height: 110px; background: var(--plum);
  }
</style>
</head>
<body>
  <div class="card">
    <div class="brand">
      <span class="brand-dot"></span>
      <span class="brand-name">Moravel Stenwick Inc.</span>
    </div>

    <div class="person">
      <p class="person-name">Marisa Ortega Bellido BScOT(c)</p>
      <p class="person-role">Occupational Therapist</p>
    </div>

    <div class="divider"></div>

    <ul class="contact">
      <li>
        <svg class="contact-icon" viewBox="0 0 22 22" aria-hidden="true">
          <rect width="22" height="22" rx="2" fill="#7cbf3f"/>
          <path d="M7 5c1 0 2 2 2 3s-1 1-1 2 2 3 3 4 1-1 2-1 3 1 3 2-1 2-2 2C9 17 5 12 5 7c0-1 1-2 2-2z" fill="#fff"/>
        </svg>
        <span>(780) 555-0142</span>
      </li>
      <li>
        <svg class="contact-icon" viewBox="0 0 22 22" aria-hidden="true">
          <rect width="22" height="22" rx="2" fill="#7cbf3f"/>
          <rect x="4" y="6" width="14" height="10" fill="none" stroke="#fff" stroke-width="1.6"/>
          <path d="M4 6l7 6 7-6" fill="none" stroke="#fff" stroke-width="1.6"/>
        </svg>
        <span>moravelstenwick@postlynx.net</span>
      </li>
    </ul>

    <div class="band"></div>
  </div>
</body>
</html>
```